Cool website to book tickets on a fleet of amazing jets

morph bookmarlowsky.com, an aspx live web page, and marlowsky.net into a landing page and website template. Add standard web pages including a press page, board member page, key personnel page.

Target Market(s)

People booking affordable private charter

Industry/Entity Type

Aviation

Coding

Coded - Design and coding required

Number of Pages Required

5+ page

Font styles to use
Other font styles liked:
• Possibly the aviation font

Requirements
Must have
• Allow bookmarlowsky.com to function, but can alter the design of those pages. A book now button that takes you to the bookmarlowsky function page. That can be built into a one url design.
Nice to have
• Repeat some of the colors of our jet livery.

```html
<!DOCTYPE html>
<html lang="en">
<head>
<meta charset="utf-8">
<title>Marlowsky — Online Booking</title>
<link href="https://fonts.googleapis.com/css2?family=Cinzel:wght@400;600&family=Jost:wght@300;400;500;600&family=Poppins:wght@400&family=Tinos&display=swap" rel="stylesheet">
<style>
:root{
  --blue:#0c4fa8;
  --navy:#0b468f;
  --green:#7cc35a;
  --ink:#1f1f1f;
  --muted:#8a8a8a;
  --line:#d9d9d9;
  --footer:#cdcacb;
  --white:#ffffff;
  --brand:#1a58a8;
}
*{margin:0;padding:0;box-sizing:border-box}
html,body{width:1200px;height:2626px;overflow:hidden;background:var(--white)}
body{position:relative;font-family:'Jost',sans-serif;color:var(--ink)}
.abs{position:absolute}
a{text-decoration:none}

/* Hero */
.hero{left:0;top:0;width:1200px;height:665px}
.hero-scene{left:0;top:0;width:1200px;height:640px;
  background:linear-gradient(180deg,#2f7fd6 0%,#5aa3e4 28%,#8fc7ee 52%,#bcdcee 72%,#dfeaf0 100%)}
.hero-band{left:0;top:625px}

.brand{font-family:'Jost',sans-serif;font-weight:500;color:var(--brand);letter-spacing:1px;display:flex;align-items:center;gap:10px}
.brand-mark{width:14px;height:14px;background:var(--brand);border-radius:50%}
.header-brand{left:52px;top:60px;font-size:40px}

.nav{left:479px;top:72px;display:flex;gap:34px;font-size:17px;font-weight:400;color:var(--white);text-transform:uppercase;letter-spacing:.2px}
.nav a{color:inherit}
.nav .current{text-decoration:underline;text-underline-offset:5px}
.nav-plane{left:490px;top:50px}
.btn-book{left:971px;top:59px;width:176px;height:45px;border:2px solid var(--blue);border-radius:23px;
  color:var(--white);font-size:17px;display:flex;align-items:center;justify-content:center;text-transform:uppercase}

.hero-title{left:0;width:1200px;top:176px;text-align:center;font-size:56px;font-weight:600;color:var(--white);letter-spacing:-1px}
.hero-sub{left:0;width:1200px;top:258px;text-align:center;font-size:23px;font-weight:300;color:var(--white)}
.btn-learn{left:501px;top:318px;width:199px;height:52px;border-radius:26px;background:var(--blue);
  color:var(--white);font-family:'Tinos',serif;font-size:22px;display:flex;align-items:center;justify-content:center}

/* CEO */
.section-title{font-family:'Cinzel',serif;font-weight:400;text-align:center;width:1200px;left:0}
.ceo-title{top:750px;font-size:46px;color:var(--ink)}
.ceo-text{left:215px;width:770px;top:832px;text-align:center;font-size:16px;line-height:28.5px;font-weight:400;color:#2a2a2a}
.ceo-thanks{left:0;width:1200px;top:976px;text-align:center;font-size:16px;color:#2a2a2a}

/* Board */
.board{left:0;top:1101px;width:1200px;height:644px;
  background:linear-gradient(180deg,#1b58a0 0%,#0f4c96 40%,#0a4188 100%)}
.board-title{top:1156px;font-size:46px;color:var(--white)}
.card{top:1254px;width:194px;height:380px;background:var(--white);border-radius:97px;text-align:center}
.card .photo{position:absolute;left:15px;top:16px;width:164px;height:164px;border-radius:50%;
  background:radial-gradient(circle at 50% 40%,#bdbdbd 0%,#8a8a8a 55%,#4a4a4a 100%)}
.card .name{position:absolute;left:0;width:194px;top:204px;font-family:'Cinzel',serif;font-size:16px;color:#222}
.card .role{position:absolute;left:0;width:194px;top:243px;font-size:15px;color:#222}
.card .social{position:absolute;left:80px;top:293px;width:35px;height:35px;border-radius:50%;background:var(--blue)}
.arrow{top:1403px}
.board-band{left:0;top:1744px}

/* Contact */
.footer-bg{left:0;top:2235px}
.contact-card{left:225px;top:1855px;width:750px;height:466px;background:var(--white);box-shadow:0 0 18px rgba(0,0,0,.08)}
.contact-title{top:1893px;font-size:52px;color:var(--ink);letter-spacing:1px}
.field{height:51px;border:1px solid var(--line);border-radius:26px;font-family:'Poppins',sans-serif;font-size:14px;color:var(--muted);
  display:flex;align-items:center;justify-content:space-between;padding:0 16px 0 29px;background:var(--white)}
.field svg{fill:#9a9a9a}
.btn-submit{left:518px;top:2236px;width:164px;height:52px;border-radius:26px;background:var(--blue);color:var(--white);
  font-family:'Tinos',serif;font-size:22px;display:flex;align-items:center;justify-content:center;gap:14px}

/* Footer */
.footer-brand{left:0;width:1200px;top:2370px;justify-content:center;font-size:40px}
.footer-social{left:559px;top:2452px;display:flex;gap:14px}
.footer-social span{width:16px;height:16px;border-radius:50%;background:#8c8c8c;display:block}
.footer-links{left:0;width:1200px;top:2497px;display:flex;justify-content:center;gap:35px;font-size:19px;color:#2a2a2a}
.footer-links a{color:inherit}
.copyright{left:0;width:1200px;top:2553px;text-align:center;font-size:18px;color:#2a2a2a}
</style>
</head>
<body>

<header class="hero abs">
  <div class="hero-scene abs" role="img" aria-label="Grey and blue private jet parked on a beach with a palm island and blue sky behind"></div>
  <svg class="hero-band abs" width="1200" height="45" viewBox="0 0 1200 45">
    <polygon points="0,9 1200,5 1200,8 0,40" fill="var(--green)"/>
  </svg>

  <div class="brand header-brand abs"><span class="brand-mark"></span>Marlowsky</div>

  <svg class="nav-plane abs" width="26" height="16" viewBox="0 0 26 16"><path d="M0 8 L26 8 M8 1 L16 8 L8 15 M2 3 L5 8 L2 13" stroke="#fff" stroke-width="2.4" fill="none" stroke-linejoin="round"/></svg>
  <nav class="nav abs">
    <a class="current">Home</a>
    <a>Press</a>
    <a>Board Member</a>
    <a>Key Personnel</a>
  </nav>
  <a class="btn-book abs">Book Now</a>

  <h1 class="hero-title abs">Online Booking</h1>
  <p class="hero-sub abs">Unlocking the Fourth Wave of High-Speed Travel</p>
  <a class="btn-learn abs">Learn More</a>
</header>

<section class="ceo">
  <h2 class="section-title ceo-title abs">From the CEO</h2>
  <p class="ceo-text abs">Marlowsky is the culmination of a decades long journey to increase the effective speed door to door, reduce<br>carbon and noise footprint and open private aviation to more people – unlocking the fourth wave of<br>high speed travel. We will introduce disruptive personal mobility to ensure the safety of the family.<br>During past several months, COVID-19 has significantly increased the demand for our services.</p>
  <p class="ceo-thanks abs">Thank you for taking the time today to learn about this journey.</p>
</section>

<section class="board-section">
  <div class="board abs" role="img" aria-label="Blue-tinted view of a jet cockpit looking out over mountains"></div>
  <h2 class="section-title board-title abs">Board of Directors</h2>

  <svg class="arrow abs" style="left:118px" width="34" height="50" viewBox="0 0 34 50"><path d="M28 4 L8 25 L28 46" stroke="#fff" stroke-width="6" fill="none"/></svg>
  <svg class="arrow abs" style="left:1048px" width="34" height="50" viewBox="0 0 34 50"><path d="M6 4 L26 25 L6 46" stroke="#fff" stroke-width="6" fill="none"/></svg>

  <article class="card abs" style="left:173px">
    <div class="photo" role="img" aria-label="Portrait of Thomas Avery"></div>
    <div class="name">Thomas Avery</div>
    <div class="role">Chairman and CEO</div>
    <span class="social"></span>
  </article>
  <article class="card abs" style="left:393px">
    <div class="photo" role="img" aria-label="Portrait of Paul Demarco"></div>
    <div class="name">Paul Demarco</div>
    <div class="role">Founder Horizon, NSI,</div>
    <span class="social"></span>
  </article>
  <article class="card abs" style="left:614px">
    <div class="photo" role="img" aria-label="Portrait of Evan Lindqvist"></div>
    <div class="name">Evan Lindqvist</div>
    <div class="role">GreenPath Aero,</div>
    <span class="social"></span>
  </article>
  <article class="card abs" style="left:834px">
    <div class="photo" role="img" aria-label="Portrait of Daniel Trevor"></div>
    <div class="name">Daniel Trevor</div>
    <div class="role">Aviation Consultant,</div>
    <span class="social"></span>
  </article>

  <svg class="board-band abs" width="1200" height="36" viewBox="0 0 1200 36">
    <polygon points="0,0 1200,0 1200,3 0,34" fill="var(--green)"/>
  </svg>
</section>

<svg class="footer-bg abs" width="1200" height="391" viewBox="0 0 1200 391">
  <path d="M0 0 Q600 40 1200 -2 L1200 391 L0 391 Z" fill="var(--footer)"/>
</svg>

<section class="contact">
  <div class="contact-card abs"></div>
  <h2 class="section-title contact-title abs">Connect With Us</h2>

  <div class="field abs" style="left:258px;top:2023px;width:330px">First Name
    <svg width="15" height="16" viewBox="0 0 15 16"><circle cx="7.5" cy="4.5" r="4"/><path d="M0 16 Q0 9 7.5 9 Q15 9 15 16 Z"/></svg></div>
  <div class="field abs" style="left:606px;top:2023px;width:330px">Last Name
    <svg width="15" height="16" viewBox="0 0 15 16"><circle cx="7.5" cy="4.5" r="4"/><path d="M0 16 Q0 9 7.5 9 Q15 9 15 16 Z"/></svg></div>
  <div class="field abs" style="left:258px;top:2090px;width:330px">Email ID
    <svg width="17" height="13" viewBox="0 0 17 13"><rect width="17" height="13" rx="1"/><path d="M0 1 L8.5 7.5 L17 1" stroke="#fff" stroke-width="1.5" fill="none"/></svg></div>
  <div class="field abs" style="left:606px;top:2090px;width:330px">Phone Number
    <svg width="15" height="15" viewBox="0 0 15 15"><path d="M3 0 L6 3.5 L4.3 5.6 Q6 9 9.4 10.7 L11.5 9 L15 12 L12.7 14.8 Q6 14 2 9 Q-1 4 0.5 2 Z"/></svg></div>
  <div class="field abs" style="left:259px;top:2160px;width:678px;font-size:13px">Message
    <svg width="17" height="13" viewBox="0 0 17 13"><rect width="17" height="13" rx="1"/><path d="M0 1 L8.5 7.5 L17 1" stroke="#fff" stroke-width="1.5" fill="none"/></svg></div>

  <a class="btn-submit abs">Submit
    <svg width="16" height="16" viewBox="0 0 16 16"><circle cx="8" cy="8" r="8" fill="#fff"/><path d="M6.5 4.5 L10 8 L6.5 11.5" stroke="var(--blue)" stroke-width="2" fill="none"/></svg></a>
</section>

<footer>
  <div class="brand footer-brand abs"><span class="brand-mark"></span>Marlowsky</div>
  <div class="footer-social abs"><span></span><span></span><span></span></div>
  <nav class="footer-links abs">
    <a>Home</a><a>Press</a><a>board member</a><a>key personnel</a><a>Book now</a>
  </nav>
  <p class="copyright abs">Copyright 2020 marlowsky.net.&nbsp; All Rights Reserved.</p>
</footer>

</body>
</html>
```